Label Design Refresh for existing High End Supplement line

Design a label for our high end supplement brand, packaged in a Cobal Blue bottle.... using Clear labels as the label stock media.

A clear label design will take advantage of the blue bottle and can incorporate any design element you create, metalic elements, new graphics etc.

our line spans 50 different product categories and over 400 unique SKUs, so any elements you suggest to differentiate products or categories will be appreciated.

see: www.velmorahealth.com
Updates

Need designers to meet project requirements. Full label, clear label stock design (clear background with exception for design elements and text etc.)

Target Market(s)

Men and Women 25-55 Health conscious and not price sensitive. Product is 5x higher cost than competition.

Industry/Entity Type

Sexual health for men and women. testosterone, hormone health, nootropics

Font styles to use
Sans Serif

Colors

Designer to choose colors to be used in the design.

Requirements
Must have
• Clear label design for Cobalt blue, packer style, pharma bottle. Must feature Velmora brand on front panel. Must show entire label panel design as 2.8in x 7.25in. Graphics can be full color with metalic or foil type elements.
Nice to have
• Name of products include: SHBG, Testosterone & Libido, Adrenal Support Phase 2, LH Formula, ADHD Phase1,
Should not have
• Busy designs that are stock images for supplement label layouts

```html
<!DOCTYPE html>
<html lang="en">
<head>
<meta charset="utf-8">
<title>Velmora SHBG Mens Formula – Label</title>
<link rel="stylesheet" href="https://fonts.googleapis.com/css2?family=Roboto:wght@400;500;700&display=swap">
<style>
  :root {
    --page: #ffffff;
    --panel-grey: #e6e6e6;
    --panel-white: #f8f8f8;
    --brand-teal: #2c4a57;
    --band-navy: #042d42;
    --band-fade: #5b7b86;
    --accent-blue: #0a56b0;
    --ink: #111111;
    --on-dark: #ffffff;
  }
  html, body {
    margin: 0;
    width: 1200px;
    height: 1200px;
    overflow: hidden;
    background: var(--page);
  }
  .canvas {
    width: 1200px;
    height: 1200px;
    display: flex;
    align-items: center;
    justify-content: center;
  }
  .label {
    width: 1000px;
    height: 1122px;
    display: block;
    font-family: "Roboto", sans-serif;
  }
  .label__grey { fill: var(--panel-grey); }
  .label__white { fill: var(--panel-white); }
  .label__curve { fill: none; stroke: var(--accent-blue); stroke-width: 5; }
  .brand-name {
    fill: var(--brand-teal);
    font-weight: 700;
    font-size: 126px;
    letter-spacing: -2px;
    text-transform: uppercase;
  }
  .product-name {
    fill: var(--on-dark);
    font-weight: 400;
    font-size: 118px;
  }
  .product-sub {
    fill: var(--on-dark);
    font-weight: 400;
    font-size: 30px;
    letter-spacing: 6px;
  }
  .count {
    fill: var(--ink);
    font-weight: 400;
    font-size: 27px;
  }
  .supplement {
    fill: var(--ink);
    font-weight: 400;
    font-size: 22px;
  }
</style>
</head>
<body>
<main class="canvas">
  <svg class="label" viewBox="0 0 702 788" xmlns="http://www.w3.org/2000/svg">
    <defs>
      <linearGradient id="band-gradient" x1="0" y1="0" x2="1" y2="0">
        <stop offset="0" stop-color="var(--band-navy)"/>
        <stop offset="0.72" stop-color="var(--band-navy)"/>
        <stop offset="1" stop-color="var(--band-fade)"/>
      </linearGradient>
    </defs>

    <rect class="label__grey" x="0" y="0" width="702" height="788"/>
    <path class="label__white" d="M600,0 C600,150 480,212 382,212 A188,188 0 0 0 382,588 C480,588 600,640 600,788 L702,788 L702,0 Z"/>
    <path class="label__curve" d="M600,0 C600,150 480,212 382,212 A188,188 0 0 0 382,588 C480,588 600,640 600,788"/>

    <path class="product-band" fill="url(#band-gradient)" d="M385,236 L702,232 L702,558 L385,562 A163,163 0 0 1 385,236 Z"/>

    <text class="brand-name" transform="translate(142,690) rotate(-90)" textLength="620" lengthAdjust="spacingAndGlyphs">Velmora</text>

    <text class="product-name" x="300" y="425">SHBG</text>
    <text class="product-sub" x="304" y="470" textLength="318">MENS FORMULA</text>

    <text class="count" x="290" y="680">60 VEGETABLE</text>
    <text class="count" x="290" y="712">CAPSULES</text>
    <text class="supplement" x="290" y="748">DIETARY SUPPLEMENT</text>
  </svg>
</main>
</body>
</html>
```